Postcard needed for expert witness service

Looking for a professional postcard that will be mailed to personal injury lawyers / law firms to introduce my expert witness services.

Target Market(s)

Law firms, personal injury lawyers

Industry/Entity Type

Expert witness, law

Font styles to use
Sans Serif

Requirements
Must have
• Logo: The Frost Counsel [Main Heading]Do you handle snow and ice related slip and falls? Darrel is one of the top snow industry experts in the country! [Following should be in a list type fashion, possibly bulleted]Darrel's credentials: Accredited Winter Practitioner (AWP), past WRTA board member and chair, former ISO 9001 certified snow company owner , 32 years in the industry. (555) 284-3917 NOTES: Postcard will be 4" x 6" Please use both sides however must have room for labels and stamp
Should not have
• Wouldn't suggest using both photos on same side. Honestly, feel free to only use one of the slip and fall photos if it works out better. Thanks!

```html
<!DOCTYPE html>
<html lang="en">
<head>
<meta charset="utf-8">
<title>The Frost Counsel – Postcard</title>
<link rel="stylesheet" href="https://fonts.googleapis.com/css2?family=Righteous&family=Crimson+Text:ital,wght@0,400;0,600;1,400&display=swap">
<style>
  :root {
    --board: #cfcfcf;
    --paper: #ffffff;
    --ink: #222222;
    --ring: #19b3ea;
    --sky: #00aeef;
    --navy-band: #1f6fad;
    --bright-band: #0a93d8;
    --head-dark: #1e5fa8;
    --head-light: #3aa0e0;
    --question: #a9e2f8;
    --plum: #8e2d98;
    --brand-blue: #18a6e0;
    --dot-pale: #d4eefb;
    --dot-mid: #9fdcf6;
    --dot-deep: #5cc7f2;
    --panel: #bfe7f9;
    --stamp-line: #9a9a9a;
  }
  * { margin: 0; padding: 0; box-sizing: border-box; }
  html, body { width: 1200px; height: 450px; overflow: hidden; background: var(--board); }
  .board { position: relative; width: 1200px; height: 450px; }

  .card {
    position: absolute; top: 37.5px; width: 564px; height: 375px;
    background: var(--paper); overflow: hidden;
  }
  .card--front { left: 25.5px; }
  .card--back { left: 611px; }
  .card svg.shapes { position: absolute; inset: 0; }

  .photo { position: absolute; border-radius: 50%; }
  .photo--fall-one { left: 1px; top: -11px; width: 172px; height: 172px;
    background: radial-gradient(circle at 40% 45%, #8c8f96, #4b4540 60%, #2f3a52); }
  .photo--fall-two { left: 51px; top: 159px; width: 146px; height: 146px;
    background: radial-gradient(circle at 50% 45%, #b8bec6, #5f6670 60%, #2e3a55); }

  .brand {
    position: absolute; font-family: "Crimson Text", serif; font-weight: 600;
    white-space: nowrap; line-height: 1;
  }
  .brand--front { left: 387px; top: 36px; transform: translateX(-50%); font-size: 44px; color: var(--ink); }
  .brand--back { left: 196px; top: 318px; font-size: 27px; color: var(--brand-blue); }

  .question-mark {
    position: absolute; left: 410px; top: 82px; font-family: "Righteous", sans-serif;
    font-size: 104px; line-height: 1; color: var(--question);
  }
  .headline { position: absolute; font-family: "Righteous", sans-serif; white-space: nowrap; line-height: 1; }
  .headline .dark { color: var(--head-dark); }
  .headline .light { color: var(--head-light); }
  .headline .small { font-size: 15px; }
  .headline--1 { left: 264px; top: 108px; font-size: 18px; }
  .headline--2 { left: 273px; top: 126px; font-size: 22px; }
  .headline--3 { left: 242px; top: 148px; font-size: 22px; }
  .headline--4 { left: 295px; top: 169px; font-size: 22px; }

  .intro { position: absolute; font-family: "Crimson Text", serif; font-style: italic; font-size: 16px; line-height: 18px; color: var(--plum); white-space: nowrap; }
  .intro--1 { left: 204px; top: 192px; }
  .intro--2 { left: 231px; top: 209px; }

  .credentials { position: absolute; right: 26px; top: 229px; font-family: "Crimson Text", serif; color: var(--ink); text-align: right; }
  .credentials__title { font-style: italic; font-size: 15px; line-height: 18px; margin-right: 17px; }
  .credentials__list { list-style: none; font-size: 14.5px; line-height: 18.5px; }
  .credentials__list li::after { content: "●"; font-size: 9px; margin-left: 8px; position: relative; top: -2px; }

  .phone { position: absolute; font-family: "Crimson Text", serif; white-space: nowrap; line-height: 1; }
  .phone--front { right: 24px; top: 327px; font-size: 18px; font-style: italic; color: #ffffff; }
  .phone--back { left: 420px; top: 322px; font-size: 18px; color: var(--brand-blue); }
</style>
</head>
<body>
<div class="board">

  <section class="card card--front">
    <svg class="shapes" viewBox="0 0 564 375" width="564" height="375">
      <g class="dots">
        <circle cx="214" cy="44" r="9" fill="var(--dot-pale)"/>
        <circle cx="222" cy="146" r="17" fill="var(--dot-mid)"/>
        <circle cx="18" cy="192" r="8" fill="var(--dot-pale)"/>
        <circle cx="34" cy="300" r="15" fill="var(--dot-deep)"/>
        <circle cx="218" cy="290" r="7" fill="var(--dot-mid)"/>
        <circle cx="172" cy="332" r="11" fill="var(--dot-pale)"/>
        <circle cx="102" cy="340" r="6" fill="var(--sky)"/>
      </g>
      <g fill="none">
        <circle cx="87" cy="75" r="90" stroke="var(--ring)" stroke-width="1.5"/>
        <circle cx="124" cy="232" r="77" stroke="var(--ring)" stroke-width="1.5"/>
      </g>
      <rect x="0" y="351" width="564" height="24" fill="var(--navy-band)"/>
      <polygon points="364,351 564,351 564,375 340,375" fill="var(--bright-band)"/>
      <polygon points="388,322 564,322 564,351 364,351" fill="var(--sky)"/>
    </svg>
    <div class="photo photo--fall-one" role="img" aria-label="Photo: woman in winter coat slipping on an icy sidewalk"></div>
    <div class="photo photo--fall-two" role="img" aria-label="Photo: person falling on a wet icy pavement with a bag"></div>

    <div class="brand brand--front">The Frost Counsel</div>

    <div class="question-mark" aria-hidden="true">?</div>
    <div class="headline headline--1"><span class="dark">Do You</span></div>
    <div class="headline headline--2"><span class="dark">Handle Snow</span></div>
    <div class="headline headline--3"><span class="light small">and </span><span class="light">Ice Related Slip</span></div>
    <div class="headline headline--4"><span class="light small">and </span><span class="light">Falls</span></div>

    <p class="intro intro--1">Darrel is one of the top</p>
    <p class="intro intro--2">snow industry experts in the country!</p>

    <div class="credentials">
      <p class="credentials__title">Darrel's Credentials:</p>
      <ul class="credentials__list">
        <li>Accredited Winter Practitioner (AWP)</li>
        <li>Past WRTA board member and chair</li>
        <li>Former ISO 9001 certified snow company owner</li>
        <li>32 years in the industry</li>
      </ul>
    </div>

    <p class="phone phone--front">(555) 284-3917</p>
  </section>

  <section class="card card--back">
    <svg class="shapes" viewBox="0 0 564 375" width="564" height="375">
      <path d="M0 0 H176 C176 120 110 230 0 262 Z" fill="var(--panel)"/>
      <path d="M0 0 H190 C190 128 118 244 0 278" fill="none" stroke="var(--ring)" stroke-width="1.5"/>
      <g class="dots">
        <circle cx="212" cy="150" r="12" fill="var(--dot-pale)"/>
        <circle cx="150" cy="262" r="16" fill="var(--dot-mid)"/>
        <circle cx="40" cy="318" r="9" fill="var(--dot-deep)"/>
        <circle cx="108" cy="340" r="6" fill="var(--dot-pale)"/>
      </g>
      <rect class="stamp-box" x="439.5" y="39.5" width="82" height="92" fill="none" stroke="var(--stamp-line)" stroke-width="1"/>
      <line x1="405" y1="308" x2="405" y2="352" stroke="var(--brand-blue)" stroke-width="1.5"/>
    </svg>

    <div class="brand brand--back">The Frost Counsel</div>
    <p class="phone phone--back">(555) 284-3917</p>
  </section>

</div>
</body>
</html>
```